Design signage & window art that screams: “This is the place for wall decor!”

Contest Goal:
Design a single, cohesive storefront signage system for Ontario Decor. That includes the top fascia and bottom window graphics, presented as one polished connected visual package. Designers will provide a composite mock-up showing how the overall design looks in context.

***All Designs need to creatively incorporate the torn paper effect where the showroom is located .Example found attached(Window-Graphics_Inspo.jpg)

Category taglines
Each product section (at the bottom of each window group) should include bold, eye-catching taglines. Use the examples below — final wording may be refined later.
Window image focus clarified
Left side: Product closeups and detail shots
Right side: Lifestyle/in-room imagery

2. Layout Specifications/Dimensions
Fascia: 148 ft wide × 4 ft high
Regular windows: approx. 49” × 36”
Door glass: approx. 75” × 30”
Yellow zone (NewStorefrnt.png): Showroom windows + doors — must preserve visibility
Blue zones: All windows eligible for full-coverage graphics
Assets:
Lakeview Interiors Logo File(remove bottom text please)
Wallpaper,Mural and Panels Images in their own Zip files

3. Fascia Signage (Top Strip)
Background: Solid black or deep charcoal
Font: Bold, modern, highly legible Silver/white is preferred.
Left-aligned text layout (in this order):
Wallpaper
Murals
Panels
BrindlewallStudio.com
Lakeview Interiors (just the logo,it must be the same size as other top font)
Note: Do not include any taglines with the Lakeview Interiors logo — the product categories are already clearly spelled out.

4. Window Graphics (Lower Section)
Design a seamless visual layout across the storefront windows that reflects each product category. Each window section must line up directly below its corresponding fascia label.
Section Breakdown:
Wallpaper
Visuals: Close-up patterns, roll textures, product shots
Tagline: Don’t Paint Over Potential. Wallpaper It.
Murals
Visuals: Large-scale mural applications, dramatic visuals
Tagline: Mural of the Story? Your Walls Matter.
Panels
Visuals: Slat walls, acoustic panels, product installations
Tagline: Slat Happens. We got you covered!

5. Showroom Zone (Yellow Area in Layout)
Apply the torn-paper effect from Window-Graphics_Inspo.jpg within the yellow showroom area
This should simulate a dramatic peel-back revealing the showroom interior while maintaining clear visibility and fitting seamlessly with the surrounding design.

6. Visual Structure Guide
Left windows: Product closeups and material textures
Right windows: Styled room scenes and optional torn-paper aesthetic (some torn effect could be used on the left side too, if it works compositionally)
Taglines: Must be visually emphasized in each section
Overall layout should be clean, balanced, and contemporary

7. Final Goals
Maintain alignment between fascia text and window content
Keep the entrance clean and unobstructed
Communicate Lakeview Interiors’s brand clearly: modern, bold, and functional

Target Market(s)

Homeowners, interior designers, contractors, and DIY renovators looking for premium wall decor solutions such as wallpaper, decorative panels, and murals. Most customers are style-conscious, value design, and want to enhance living or commercial spaces with bold, modern decor elements.

Industry/Entity Type

Interior Design / Home Improvement / Retail

Requirements
Must have
• • A single cohesive design that integrates both the top signage and window graphics • The text: “Brindlewallstudio.com | Panels | Wallpaper | Murals” plus the Lakeview Interiors logo • High legibility from a distance (ideal for street traffic) • A clear, well-lit showroom entrance (yellow-marked section must stay mostly transparent) •The torn paper effect(Window-Graphics_Inspo.jpg) • Visual alignment between fascia and windows (should feel like one system)
Nice to have
• Use of subtle framing, transparency, or frosted effects to blend the entrance into the full design • Modern typography and layout styles • Elements inspired by included reference files (especially “BottomIdeaInspo” and “Window-Graphics”) • Visual references to wallpaper, panels, or mural-style art in the window graphics • A few creative layout options or variations of the final concept (if time allows)
Should not have
• Should not haves • Cluttered or overly busy designs • Serif or ornate fonts that are hard to read at a distance • Fully opaque designs on the showroom entrance • Literal or outdated imagery(provided in WallpaperMuralAndPanelImages.zip they are supposed to help guide your design,Please dont only use those as the images) — the overall tone should be bold and modern, not traditional

```html
<!DOCTYPE html>
<html lang="en">
<head>
<meta charset="utf-8">
<title>Lakeview Interiors – Storefront Signage</title>
<link href="https://fonts.googleapis.com/css2?family=Roboto+Condensed:wght@300;400;700;800&display=swap" rel="stylesheet">
<style>
  :root{
    --canvas:#ffffff;
    --frame:#d0d0d0;
    --grid:#6b6b6b;
    --fascia:#231a17;
    --fascia-text:#ffffff;
    --window-edge:#e3262d;
    --showroom:#fdf5a0;
    --gold:#c9a24a;
    --paper-edge:#f4ecd6;
    --paper-back:#efe6cf;
    --tag-shadow:rgba(0,0,0,.85);
  }
  *{margin:0;padding:0;box-sizing:border-box}
  html,body{width:1200px;height:600px;overflow:hidden;background:var(--canvas)}
  .storefront{position:relative;width:1200px;height:600px;border:1px solid var(--frame);background:var(--canvas);font-family:"Roboto Condensed",Arial,sans-serif}
  .elevation{position:absolute;left:0;top:0;width:1200px;height:600px}
  .fascia-label{position:absolute;top:280px;color:var(--fascia-text);font-weight:700;font-size:27px;line-height:27px;letter-spacing:1px;white-space:nowrap}
  .fascia-label.tight{letter-spacing:-1px}
  .fascia-label .chevron{font-size:18px;vertical-align:4px;margin-right:4px;letter-spacing:0}
  .fascia-contact{position:absolute;top:284px;color:var(--fascia-text);font-weight:300;line-height:20px;white-space:nowrap}
  .fascia-contact.web{font-size:16px;letter-spacing:.6px}
  .fascia-contact.phone{font-size:17px;letter-spacing:.8px}
  .chevron-solo{position:absolute;top:283px;color:var(--fascia-text);font-weight:700;font-size:18px}
  .brand-name{position:absolute;top:285px;left:985px;color:var(--fascia-text);font-weight:400;font-size:14px;line-height:20px;letter-spacing:.3px;white-space:nowrap}
  .tagline{position:absolute;text-align:center;color:#fff;font-weight:800;text-transform:uppercase;white-space:nowrap;line-height:1;
    text-shadow:-.6px -.6px 0 var(--tag-shadow),.6px -.6px 0 var(--tag-shadow),-.6px .6px 0 var(--tag-shadow),.6px .6px 0 var(--tag-shadow)}
  .tagline .lead{display:block;font-size:6.5px;margin-bottom:1.5px;letter-spacing:.2px}
  .tagline .punch{display:block;font-size:9.5px}
</style>
</head>
<body>
<div class="storefront">
  <svg class="elevation" viewBox="0 0 1200 600" xmlns="http://www.w3.org/2000/svg">
    <defs>
      <linearGradient id="g-mural" x1="0" y1="0" x2="1" y2="1"><stop offset="0" stop-color="#5f8c4c"/><stop offset="1" stop-color="#1f4a32"/></linearGradient>
      <linearGradient id="g-mural-pill" x1="0" y1="0" x2="0" y2="1"><stop offset="0" stop-color="#c8b04c"/><stop offset="1" stop-color="#3d3a2a"/></linearGradient>
      <linearGradient id="g-slat" x1="0" y1="0" x2="1" y2="0"><stop offset="0" stop-color="#6a3d22"/><stop offset="1" stop-color="#3b2214"/></linearGradient>
      <linearGradient id="g-slat-pill" x1="0" y1="0" x2="1" y2="1"><stop offset="0" stop-color="#d6b488"/><stop offset="1" stop-color="#2b2b2b"/></linearGradient>
      <linearGradient id="g-paper" x1="0" y1="0" x2="1" y2="1"><stop offset="0" stop-color="#2f7a66"/><stop offset="1" stop-color="#1f5a4c"/></linearGradient>
      <linearGradient id="g-paper-pill" x1="0" y1="0" x2="1" y2="1"><stop offset="0" stop-color="#b39467"/><stop offset="1" stop-color="#6b5436"/></linearGradient>
      <linearGradient id="g-scales" x1="0" y1="0" x2="1" y2="0"><stop offset="0" stop-color="#6f7470"/><stop offset=".35" stop-color="#3a8fa8"/><stop offset="1" stop-color="#c8a040"/></linearGradient>
      <linearGradient id="g-scales-pill" x1="0" y1="0" x2="0" y2="1"><stop offset="0" stop-color="#d8d2c6"/><stop offset="1" stop-color="#e8b422"/></linearGradient>
      <linearGradient id="g-stone" x1="0" y1="0" x2="1" y2="0"><stop offset="0" stop-color="#8a8886"/><stop offset="1" stop-color="#d0ccc4"/></linearGradient>
      <linearGradient id="g-stone-pill" x1="0" y1="0" x2="1" y2="1"><stop offset="0" stop-color="#b08a52"/><stop offset="1" stop-color="#4f4f52"/></linearGradient>
      <linearGradient id="g-damask" x1="0" y1="0" x2="1" y2="1"><stop offset="0" stop-color="#3a4740"/><stop offset="1" stop-color="#26302b"/></linearGradient>
      <linearGradient id="g-damask-pill" x1="0" y1="0" x2="0" y2="1"><stop offset="0" stop-color="#e2d6bd"/><stop offset="1" stop-color="#9e4a38"/></linearGradient>
      <linearGradient id="g-gold-texture" x1="0" y1="0" x2="1" y2="1"><stop offset="0" stop-color="#8f8262"/><stop offset="1" stop-color="#6d644e"/></linearGradient>
      <linearGradient id="g-peel" x1="0" y1="0" x2="1" y2="1"><stop offset="0" stop-color="#ffffff"/><stop offset="1" stop-color="#cfc4a6"/></linearGradient>
      <clipPath id="clip-w1"><rect x="64.3" y="314.4" width="141.1" height="66.2"/></clipPath>
      <clipPath id="clip-w2"><rect x="212" y="314.4" width="140.6" height="66.6"/></clipPath>
      <clipPath id="clip-w3"><rect x="359.6" y="315.3" width="140.7" height="65.7"/></clipPath>
      <clipPath id="clip-w4"><rect x="801.7" y="314" width="141.1" height="65.6"/></clipPath>
      <clipPath id="clip-w5"><rect x="949.3" y="314" width="108.6" height="65.6"/></clipPath>
      <clipPath id="clip-w6"><rect x="1064.4" y="314" width="70.8" height="65.6"/></clipPath>
    </defs>

    <g class="transom-grid" fill="none" stroke="var(--grid)" stroke-width="0.7">
      <rect x="64.3" y="218.5" width="141.1" height="53.1"/><path d="M99.6 218.5V271.6M134.8 218.5V271.6M170.1 218.5V271.6M64.3 245H205.4"/>
      <rect x="212" y="218.5" width="140.6" height="53.1"/><path d="M247.2 218.5V271.6M282.3 218.5V271.6M317.5 218.5V271.6M212 245H352.6"/>
      <rect x="359.6" y="218.5" width="140.7" height="53.1"/><path d="M394.8 218.5V271.6M430 218.5V271.6M465.1 218.5V271.6M359.6 245H500.3"/>
      <rect x="506.8" y="218.5" width="140.7" height="53.1"/><path d="M542 218.5V271.6M577.2 218.5V271.6M612.3 218.5V271.6M506.8 245H647.5"/>
      <rect x="654.5" y="218.5" width="140.7" height="53.1"/><path d="M689.7 218.5V271.6M724.8 218.5V271.6M760 218.5V271.6M654.5 245H795.2"/>
      <rect x="801.7" y="218.5" width="141.1" height="53.1"/><path d="M837 218.5V271.6M872.3 218.5V271.6M907.5 218.5V271.6M801.7 245H942.8"/>
      <rect x="950.7" y="218.5" width="105.8" height="53.1"/><path d="M986 218.5V271.6M1021.2 218.5V271.6M950.7 245H1056.5"/>
      <rect x="1064.4" y="218.5" width="70.4" height="53.1"/><path d="M1099.6 218.5V271.6M1064.4 245H1134.8"/>
    </g>

    <rect class="fascia" x="64.3" y="273" width="1070.9" height="40" fill="var(--fascia)"/>

    <g class="window window-murals" clip-path="url(#clip-w1)">
      <rect x="64.3" y="314.4" width="141.1" height="66.2" fill="#fff"/>
      <rect x="64.3" y="336.3" width="141.1" height="44.3" fill="url(#g-mural)" role="img" aria-label="Lush tropical leaf mural"/>
      <rect x="156.3" y="289.7" width="46" height="110" rx="23" transform="rotate(30 179.3 344.7)" fill="url(#g-mural-pill)" stroke="var(--gold)" stroke-width="1.4" role="img" aria-label="Room styled with a gold botanical mural"/>
    </g>
    <rect x="64.3" y="314.4" width="141.1" height="66.2" fill="none" stroke="var(--window-edge)" stroke-width="0.8"/>

    <g class="window window-panels" clip-path="url(#clip-w2)">
      <rect x="212" y="314.4" width="140.6" height="66.6" fill="#fff"/>
      <rect x="212" y="336.3" width="140.6" height="44.7" fill="url(#g-slat)" role="img" aria-label="Walnut slat wall panels"/>
      <rect x="300.7" y="289.7" width="46" height="110" rx="23" transform="rotate(30 323.7 344.7)" fill="url(#g-slat-pill)" stroke="var(--gold)" stroke-width="1.4" role="img" aria-label="Close-up of oak acoustic slat panels"/>
    </g>
    <rect x="212" y="314.4" width="140.6" height="66.6" fill="none" stroke="var(--window-edge)" stroke-width="0.8"/>

    <g class="window window-wallpaper" clip-path="url(#clip-w3)">
      <rect x="359.6" y="315.3" width="140.7" height="65.7" fill="#fff"/>
      <rect x="359.6" y="336.3" width="140.7" height="44.7" fill="url(#g-paper)" role="img" aria-label="Emerald marbled wallpaper texture"/>
      <rect x="447.5" y="292" width="46" height="110" rx="23" transform="rotate(30 470.5 347)" fill="url(#g-paper-pill)" stroke="var(--gold)" stroke-width="1.4" role="img" aria-label="Unrolled textured wallpaper roll"/>
    </g>
    <rect x="359.6" y="315.3" width="140.7" height="65.7" fill="none" stroke="var(--window-edge)" stroke-width="0.8"/>

    <g class="showroom">
      <rect x="506.8" y="314.4" width="288.4" height="65.2" fill="var(--showroom)"/>
      <g class="showroom-glazing" fill="none" stroke="var(--window-edge)" stroke-width="0.7">
        <path d="M506.8 314.4V360M538 314.4V360M568.8 314.4V360M599.5 314.4V360M506.8 335.4H599.5"/>
        <path d="M654.5 314.4V360M690.3 314.4V360M725.3 314.4V360M760.7 314.4V360M795.2 314.4V360M654.5 335.4H795.2"/>
      </g>

      <g class="torn-paper torn-left">
        <polyline points="506.8,355.8 512,353.3 518,357.4 524,354 531,357.8 537,354.6 544,357 550,353.6 557,357.6 563,354.8 570,358 576,354.2 583,357.2 589,354.4 594,356.8 599.5,355.3" fill="none" stroke="var(--paper-edge)" stroke-width="2.2" stroke-linejoin="round"/>
        <path d="M506.8 379.6V357L512 354.5L518 358.6L524 355.2L531 359L537 355.8L544 358.2L550 354.8L557 358.8L563 356L570 359.2L576 355.4L583 358.4L589 355.6L594 358L599.5 356.5V379.6Z" fill="url(#g-gold-texture)" role="img" aria-label="Gold linework wallpaper torn back from the showroom glass"/>
        <path d="M599.5 356.5L599.5 369L589.5 358.5Z" fill="url(#g-peel)" stroke="var(--gold)" stroke-width="0.5"/>
      </g>
      <g class="torn-paper torn-right">
        <polyline points="654.5,355.8 661,353.4 668,357.4 675,354 682,357.8 689,354.4 696,357 703,353.6 710,357.6 717,354.6 724,357.8 731,354 738,357.2 745,354.4 752,357.6 759,353.8 766,357 773,354.4 780,357.6 787,354 795.2,356.4" fill="none" stroke="var(--paper-edge)" stroke-width="2.2" stroke-linejoin="round"/>
        <path d="M654.5 379.6V357L661 354.6L668 358.6L675 355.2L682 359L689 355.6L696 358.2L703 354.8L710 358.8L717 355.8L724 359L731 355.2L738 358.4L745 355.6L752 358.8L759 355L766 358.2L773 355.6L780 358.8L787 355.2L795.2 357.6V379.6Z" fill="url(#g-gold-texture)" role="img" aria-label="Gold linework wallpaper torn back from the showroom glass"/>
        <path d="M654.5 357L654.5 369L664.5 358.2Z" fill="url(#g-peel)" stroke="var(--gold)" stroke-width="0.5"/>
      </g>

      <g class="door" fill="none" stroke="var(--window-edge)" stroke-width="0.7">
        <rect x="604.2" y="328.4" width="44.7" height="48"/>
        <path d="M626.5 328.4V376.4"/>
        <rect x="607.9" y="332.1" width="15.9" height="18.2"/><rect x="607.9" y="354.5" width="15.9" height="18.2"/>
        <rect x="629.4" y="332.1" width="15.9" height="18.2"/><rect x="629.4" y="354.5" width="15.9" height="18.2"/>
      </g>
    </g>

    <g class="window window-lifestyle" clip-path="url(#clip-w4)">
      <rect x="801.7" y="314" width="141.1" height="65.6" fill="#fff"/>
      <rect x="801.7" y="336.3" width="141.1" height="43.3" fill="url(#g-scales)" role="img" aria-label="Teal and gold scale-pattern feature wall"/>
      <rect x="890" y="289.7" width="46" height="110" rx="23" transform="rotate(30 913 344.7)" fill="url(#g-scales-pill)" stroke="var(--gold)" stroke-width="1.4" role="img" aria-label="Living room with a mustard velvet sofa"/>
    </g>
    <rect x="801.7" y="314" width="141.1" height="65.6" fill="none" stroke="var(--window-edge)" stroke-width="0.8"/>

    <g class="window window-lifestyle" clip-path="url(#clip-w5)">
      <rect x="949.3" y="314" width="108.6" height="65.6" fill="#fff"/>
      <rect x="949.3" y="336.3" width="108.6" height="43.3" fill="url(#g-stone)" role="img" aria-label="Soft grey lounge with a tree mural"/>
      <rect x="1006.5" y="289.7" width="46" height="110" rx="23" transform="rotate(30 1029.5 344.7)" fill="url(#g-stone-pill)" stroke="var(--gold)" stroke-width="1.4" role="img" aria-label="Stacked metallic wallpaper rolls"/>
    </g>
    <rect x="949.3" y="314" width="108.6" height="65.6" fill="none" stroke="var(--window-edge)" stroke-width="0.8"/>

    <g class="window window-lifestyle" clip-path="url(#clip-w6)">
      <rect x="1064.4" y="314" width="70.8" height="65.6" fill="#fff"/>
      <rect x="1064.4" y="336.3" width="70.8" height="43.3" fill="url(#g-damask)" role="img" aria-label="Dark green damask wallpaper"/>
      <rect x="1097.6" y="292.4" width="36" height="100" rx="18" transform="rotate(30 1115.6 342.4)" fill="url(#g-damask-pill)" stroke="var(--gold)" stroke-width="1.4" role="img" aria-label="Oriental landscape mural panel"/>
    </g>
    <rect x="1064.4" y="314" width="70.8" height="65.6" fill="none" stroke="var(--window-edge)" stroke-width="0.8"/>
  </svg>

  <div class="fascia-label" style="left:73px"><span class="chevron">»</span>MURALS</div>
  <div class="fascia-label" style="left:223px"><span class="chevron">»</span>PANELS</div>
  <div class="fascia-label tight" style="left:359px"><span class="chevron">»</span>WALLPAPER</div>
  <span class="chevron-solo" style="left:542px">»</span>
  <div class="fascia-contact web" style="left:560px">www.brindlewallstudio.com</div>
  <span class="chevron-solo" style="left:810px">»</span>
  <div class="fascia-contact phone" style="left:836px">(555) 214-7390</div>
  <span class="chevron-solo" style="left:962px">»</span>
  <div class="brand-name">LAKEVIEW INTERIORS</div>

  <div class="tagline" style="left:66px;width:84px;top:357px"><span class="lead">Mural of Story?</span><span class="punch">Your Walls Matter</span></div>
  <div class="tagline" style="left:212px;width:84px;top:356px"><span class="lead">Slat Happens</span><span class="punch">We'll Cover It</span></div>
  <div class="tagline" style="left:362px;width:84px;top:355px"><span class="lead">Don't Paint Over Potential.</span><span class="punch">Wallpaper It.</span></div>
</div>
</body>
</html>
```